Stationary design for real estate company in Trinidad and Tobago

Kestra Realty Ltd. , real estate company operating in Trinidad and Tobago, requires a sleek, modern and professional stationary package to wow our customers and potential new clients. we want to look sleek and professional; first impressions count in this business!
Business Address:
Level 1, Marlowe Point Tower
4C Seldon Grove Boulevard
Marlowe Point
Colwyn Pereira Highway
Port of Spain
Trinidad
Tel: + 1 868 555 0147
www.kestra-tt.com
info@kestra-tt.com

```html
<!DOCTYPE html>
<html lang="en">
<head>
<meta charset="utf-8">
<title>Kestra Realty – Business Card</title>
<link href="https://fonts.googleapis.com/css2?family=Arimo:wght@400;700&display=swap" rel="stylesheet">
<style>
  :root{
    --navy:#142f57;
    --navy-light:#1d3f69;
    --navy-deep:#132f59;
    --gold:#b8975a;
    --paper:#f5f5f6;
    --backdrop:#e4e4e4;
    --ink-white:#ffffff;
    --emboss:#5f88b0;
  }
  *{margin:0;padding:0;box-sizing:border-box}
  html,body{width:1200px;height:1200px;overflow:hidden}
  body{background:var(--backdrop);font-family:"Arimo",Arial,sans-serif;position:relative}
  .card{position:absolute;left:262px;width:686px;height:392px;border-radius:20px;overflow:hidden}
  .card--front{top:165px;background:var(--navy)}
  .card--back{top:653px;background:linear-gradient(180deg,var(--navy-light),var(--navy-deep))}
  .front-shape{position:absolute;inset:0;width:100%;height:100%}
  .contact{position:absolute;left:44px;top:50px;color:var(--ink-white);font-size:17px;line-height:21.5px}
  .contact__name{color:var(--gold);font-weight:700;font-size:26px;line-height:30px}
  .contact__role{margin-bottom:18px}
  .contact__block{margin-bottom:10px}
  .contact__lines{margin-top:14px}
  .contact__line{display:flex;align-items:center;gap:9px}
  .contact__icon{width:14px;height:14px;flex:none}
  .brand{position:absolute;display:flex;align-items:center;gap:10px;font-weight:700;letter-spacing:2px}
  .brand__dot{border-radius:50%;background:var(--gold);flex:none}
  .brand--front{left:400px;top:178px;color:var(--navy);font-size:40px}
  .brand--front .brand__dot{width:22px;height:22px}
  .brand--back{left:0;right:0;top:168px;justify-content:center;color:var(--emboss);font-size:62px;letter-spacing:4px}
</style>
</head>
<body>
  <section class="card card--front">
    <svg class="front-shape" viewBox="0 0 686 392" aria-hidden="true">
      <circle cx="505" cy="195" r="212" fill="var(--paper)"/>
      <path d="M 355 45 A 212 212 0 0 0 470 405" fill="none" stroke="var(--gold)" stroke-width="4"/>
      <path d="M 505 -17 A 212 212 0 0 1 630 20" fill="none" stroke="var(--gold)" stroke-width="2"/>
      <rect x="560" y="0" width="126" height="392" fill="var(--paper)"/>
    </svg>
    <div class="contact">
      <div class="contact__name">Marcus Ellery</div>
      <div class="contact__role">President</div>
      <div class="contact__block">Level 1, Marlowe Point Tower<br>4C Seldon Grove Boulevard<br>Marlowe Point</div>
      <div>Colwyn Pereira Highway<br>Port of Spain<br>Trinidad</div>
      <div class="contact__lines">
        <div class="contact__line">
          <svg class="contact__icon" viewBox="0 0 24 24"><path fill="var(--gold)" d="M6.6 10.8c1.4 2.8 3.8 5.1 6.6 6.6l2.2-2.2c.3-.3.7-.4 1-.2 1.1.4 2.3.6 3.6.6.6 0 1 .4 1 1V20c0 .6-.4 1-1 1C10.6 21 3 13.4 3 4c0-.6.4-1 1-1h3.5c.6 0 1 .4 1 1 0 1.3.2 2.5.6 3.6.1.3 0 .7-.2 1z"/></svg>
          <span>+ 1 868 555 0147</span>
        </div>
        <div class="contact__line">
          <svg class="contact__icon" viewBox="0 0 24 24"><path fill="var(--gold)" d="M2 5h20v14H2z"/><path d="M2 5l10 8 10-8" fill="none" stroke="var(--navy)" stroke-width="2"/></svg>
          <span>info@kestra-tt.com</span>
        </div>
        <div class="contact__line">
          <svg class="contact__icon" viewBox="0 0 24 24"><circle cx="12" cy="12" r="10" fill="var(--gold)"/><path d="M2 12h20M12 2c3 3 3 17 0 20M12 2c-3 3-3 17 0 20" fill="none" stroke="var(--navy)" stroke-width="1.5"/></svg>
          <span>www.kestra-tt.com</span>
        </div>
      </div>
    </div>
    <div class="brand brand--front"><span class="brand__dot"></span><span>KESTRA REALTY</span></div>
  </section>

  <section class="card card--back">
    <div class="brand brand--back"><span>KESTRA REALTY</span></div>
  </section>
</body>
</html>
```